Design a label for a dog shampoo names plovik, the sell point of this series of shampoo is “just like wash your dogs with milk, not harm for your hand ”, the style could be gentle or professional or even amazing.

Use only 2 colors in the design job, the color of our logo could be changed, it depends on your whole page. Please design in CDR or ai.

update:
Pls do more change with the fonts when you design the front page, including title and details. Try more styles of fonts. Addition, this design will be printed on the bottle, no a label stick on it.
Updates

Do not put a real dog or animal on the page, Pay more attention to the types of fonts

Reason: Expect for more design idea.

Target Market(s)

people 20-30 years old who have dogs and cats at home

Industry/Entity Type

It Professional

Requirements
Nice to have
• It would be nice if you add some detail words in the design of the right side.

```html
<!DOCTYPE html>
<html lang="en">
<head>
<meta charset="utf-8">
<title>plovik – Super-conditioning &amp; nutrient shampoo label</title>
<link rel="stylesheet" href="https://fonts.googleapis.com/css2?family=Alfa+Slab+One&family=Crimson+Text:wght@400;600&family=PT+Serif:wght@400;700&display=swap">
<style>
  :root{
    --teal:#00aecb;
    --teal-text:#17a8c3;
    --cream:#fbf6c3;
    --paper:#ffffff;
    --backdrop-light:#f7f7f7;
    --backdrop-dark:#e2e2e2;
    --edge:#d9d9d9;
  }
  *{margin:0;padding:0;box-sizing:border-box}
  html,body{width:1200px;height:846px;overflow:hidden}
  body{background:radial-gradient(ellipse at 50% 35%,var(--backdrop-light) 0%,var(--backdrop-dark) 100%)}
  .stage{position:relative;width:1240px;height:874px;transform:scale(0.96774);transform-origin:0 0}
  .label{position:absolute;top:97px;width:353px;height:679px;background:var(--paper);border:1px solid var(--edge);border-radius:22px;box-shadow:0 2px 6px rgba(0,0,0,.12);overflow:hidden}
  .label--front{left:222px}
  .label--back{left:665px}
  .bands{position:absolute;left:0;top:0;width:353px;height:679px}
  .brand-name{position:absolute;left:0;width:353px;text-align:center;font-family:"Alfa Slab One",serif;color:var(--cream);font-weight:400;letter-spacing:1px;line-height:1}
  .label--front .brand-name{top:74px;font-size:40px}
  .label--back .brand-name{top:44px;font-size:24px}

  .product-title{position:absolute;top:204px;left:0;width:353px;text-align:center;font-family:"Alfa Slab One",serif;font-weight:400;color:var(--teal);font-size:26px;line-height:29px}
  .tagline{position:absolute;top:273px;left:0;width:353px;text-align:center;font-family:"Crimson Text",serif;color:var(--teal);font-size:17px;line-height:18px}
  .dog-art{position:absolute;left:34px;top:312px;width:288px;height:160px;border-radius:40px 60px 20px 20px;background:radial-gradient(ellipse at 55% 55%,var(--cream) 0%,var(--cream) 35%,#9fdbe6 60%,var(--teal) 100%)}
  .benefits{position:absolute;top:476px;left:0;width:353px;text-align:center;font-family:"Alfa Slab One",serif;color:var(--teal);font-size:18px;line-height:19px}
  .volume{position:absolute;top:592px;left:0;width:353px;text-align:center;font-family:"Alfa Slab One",serif;color:var(--paper);font-size:34px;line-height:1;letter-spacing:1px}

  .details{position:absolute;top:130px;left:19px;width:316px;font-family:"PT Serif",serif;color:var(--teal-text);font-size:11.6px;letter-spacing:.2px;line-height:12.6px;text-align:justify}
  .details p{margin-bottom:12px}
  .details strong{font-weight:700}
  .details .heading{font-weight:700;display:block}
  .details ul{list-style:none;margin-bottom:12px}
</style>
</head>
<body>
<div class="stage">

  <section class="label label--front">
    <svg class="bands" viewBox="0 0 353 679" aria-hidden="true">
      <path d="M18,45 Q18,33 30,33 L323,33 Q335,33 335,45 L335,124 Q175,116 18,152 Z" fill="var(--teal)"/>
      <path d="M18,154 Q175,118 335,128 L335,142 Q175,132 18,168 Z" fill="var(--cream)"/>
      <path d="M18,172 Q175,136 335,146 L335,150 Q175,140 18,176 Z" fill="var(--teal)"/>
      <path d="M18,520 Q175,568 335,515 L335,521 Q175,574 18,526 Z" fill="var(--teal)"/>
      <path d="M18,530 Q175,578 335,525 L335,541 Q175,594 18,546 Z" fill="var(--cream)"/>
      <path d="M18,550 Q175,598 335,545 L335,632 Q335,644 323,644 L30,644 Q18,644 18,632 Z" fill="var(--teal)"/>
    </svg>
    <div class="brand-name">plovik</div>
    <h1 class="product-title">Super-conditioning<br>&amp; nutrient shampoo</h1>
    <p class="tagline">just like wash your dogs with milk,<br>not harm for your hand</p>
    <div class="dog-art" role="img" aria-label="Silhouettes of three dogs standing together"></div>
    <p class="benefits">MOISTURE-RICH<br>SMOOTH AND<br>SILKY</p>
    <p class="volume">1000 ML</p>
  </section>

  <section class="label label--back">
    <svg class="bands" viewBox="0 0 353 679" aria-hidden="true">
      <path d="M18,45 Q18,34 30,34 L323,34 Q335,34 335,45 L335,94 Q175,74 18,82 Z" fill="var(--teal)"/>
      <path d="M18,85 Q175,77 335,97 L335,110 Q175,90 18,98 Z" fill="var(--cream)"/>
      <path d="M18,101 Q175,93 335,113 L335,117 Q175,97 18,105 Z" fill="var(--teal)"/>
      <path d="M18,578 Q175,563 335,583 L335,587 Q175,567 18,582 Z" fill="var(--teal)"/>
      <path d="M18,586 Q175,571 335,591 L335,603 Q175,583 18,598 Z" fill="var(--cream)"/>
      <path d="M18,603 Q175,588 335,608 L335,632 Q335,644 323,644 L30,644 Q18,644 18,632 Z" fill="var(--teal)"/>
    </svg>
    <div class="brand-name">plovik</div>
    <div class="details">
      <p><strong>PLOVIK Super-Conditioning &amp; Nutrient Shampoo</strong> is a specially formulated shampoo, rich in conditioners picked up from milk which subdivide and balance nutrition of pet's coat. More easier and better assimilate for coat from base to the end after using. With the help of minusion, the balancer of nutrition, rinses out quickly and completely to leave a soft, sparkling, and smooth coat. Safe and gentle enough to be used every day. Safe for even the most sensitive skin and coat, puppies, lactating bitches and cats.</p>
      <span class="heading">DERECTIONS:</span>
      <ul>
        <li>Before shampooing, blush out pet's coat.</li>
        <li>Saturate dog's coat with lukewarm water.</li>
        <li>Dispense a small amount of shampoo into the palm of your hand.</li>
        <li>To clean coat, start at dog's head and work back towards the tail. Avoid getting shampoo into the dog's eyes and ears.</li>
        <li>Rinse coat sereral times with lukewarm water.</li>
        <li>Towel dry and gently comb or brush coat.</li>
      </ul>
      <p><strong>ACTIVE INGREDIENTS:</strong> Hypochlorous Acid, Sodium Hypochlorite</p>
      <p><strong>USE PRECAUTIONS:</strong> Harmful if swallowed. Do not inhale. Discontinue use if irritation develops and contact your veterinarian. For animal use only. Not for human use. Keep out of reach of children. Do not decant into smaller containers. Not for injection. Always consult with a Veterinarian for systemic conditions.</p>
      <p><strong>STORAGE AND DISPOSAL:</strong> Keep out of the tough of children. Replace Cap. Wrap in several layers of newspaper and discard in trash.</p>
    </div>
  </section>

</div>
</body>
</html>
```